3x-Kammerhof
Zielgruppe
3x-Kammerhof.de vermietet Lagercontainern an Privatkunden und Gewerbetriebende
Vermietung von Stellfächen für Wohnmobile/Boote etc
Das ganze auf einem Gewerbegelände in Köln (Brauweiler)
Aufgabenstellung
Erstellung eines 2-Seitigen DIN lang (10,5 x 21 cm) Flyers
Seite A: Vermietung von Lagercontainern
Seite B: Stellfächen für Wohnmobile/Boote
Wichtig: Die Sicherheit (Zutrittskontrolle, Videoüberwachung, Brandmeldeanlage)
Preise sollen auf Flyern erscheinen, diese wie auch die Textee möchte ich jedoch ändern können.
Alle Texte können auch von der Seite 3x-kammerhof.de übernommen werden
Das Logo (siehe stellhof_welt.ai) müsste noch bearbeitet werden .... also "stellhofwelt" raus und dafür "Lagerraum Container" rein
Gerne mit Symbolen arbeiten ..

```html
<!DOCTYPE html>
<html lang="de">
<head>
<meta charset="utf-8">
<title>3x-Kammerhof – Flyer DIN lang</title>
<link href="https://fonts.googleapis.com/css2?family=Antonio:wght@600&family=Oswald:wght@500&family=Ubuntu:wght@400;500;700&display=swap" rel="stylesheet">
<style>
  :root{
    --navy:#132a4d;
    --red:#a51c2a;
    --white:#ffffff;
    --text:#1c2c46;
    --panel:#f1f2f4;
    --line:#132a4d;
  }
  *{box-sizing:border-box;margin:0;padding:0}
  html,body{width:1200px;height:1010px;overflow:hidden;background:#fff}
  body{position:relative;font-family:"Ubuntu",sans-serif;color:var(--text)}
  .flyer{position:absolute;top:87px;width:425px;height:851px;background:#fff;overflow:hidden;box-shadow:0 0 1px rgba(0,0,0,.2)}
  .flyer--container{left:130px}
  .flyer--stellplatz{left:644px}

  .header{position:absolute;left:0;top:0;width:100%;height:122px;background:var(--navy);display:flex;align-items:center;justify-content:center;gap:12px}
  .brand-dot{width:18px;height:18px;background:var(--red)}
  .brand-name{font-family:"Ubuntu",sans-serif;font-weight:700;font-size:36px;color:var(--white);letter-spacing:.5px}

  .claim-band{position:absolute;left:0;top:126px;width:100%;height:49px;background:var(--red);display:flex;align-items:center;justify-content:center;gap:18px;color:#fff;font-weight:500;font-size:25px}
  .claim-band span{display:flex;align-items:center;gap:7px}
  .claim-band svg{width:19px;height:19px}

  .photo{position:absolute;left:0;top:178px;width:100%;height:183px;background:linear-gradient(180deg,#b9c7d8 0%,#6b8a5c 30%,#24448f 45%,#1e3a7c 75%,#6b4a30 100%)}
  .badge{position:absolute;left:21px;top:190px;width:158px;height:158px;border-radius:50%;background:#d6d6d6;display:flex;align-items:center;justify-content:center}
  .badge-inner{width:146px;height:146px;border-radius:50%;background:#fff;display:flex;align-items:center;justify-content:center}
  .badge-core{width:134px;height:134px;border-radius:50%;background:var(--red);color:#fff;display:flex;flex-direction:column;align-items:center;justify-content:center;transform:rotate(-12deg);text-align:center;line-height:1}
  .badge-core .big{font-family:"Oswald",sans-serif;font-weight:500;font-size:23px}
  .badge-core .bigger{font-family:"Oswald",sans-serif;font-weight:500;font-size:27px;margin-top:1px}
  .badge-core .small{font-size:10.5px;font-weight:500;margin-top:5px;line-height:1.3}

  .section-title{position:absolute;left:0;width:100%;text-align:center;white-space:nowrap;font-family:"Antonio",sans-serif;font-weight:600;font-size:27px;line-height:1.2;color:var(--navy);letter-spacing:.3px}
  .flyer--container .section-title{top:370px}
  .flyer--stellplatz .section-title{top:188px}

  .offer-area{position:absolute;left:0;width:100%;background:linear-gradient(180deg,#fff 0%,#fff 45%,#e9ebee 100%)}
  .flyer--container .offer-area{top:412px;height:163px}
  .flyer--stellplatz .offer-area{top:225px;height:171px}
  .product-image{position:absolute;border-radius:2px}
  .flyer--container .product-image{left:27px;top:7px;width:180px;height:146px;background:linear-gradient(90deg,#203d8c 0%,#2a4ea6 45%,#b58a55 55%,#c9cbd0 75%,#e2e3e6 100%)}
  .flyer--stellplatz .product-image{left:18px;top:25px;width:185px;height:133px;background:radial-gradient(ellipse at 50% 45%,#ffffff 0%,#e4e6ea 55%,#b8bcc4 100%)}

  .price-box{position:absolute;width:188px;height:136px;background:var(--navy);border:3px solid #fff;outline:2px solid var(--navy);border-radius:4px;color:#fff;padding:10px 0 0 16px}
  .flyer--container .price-box{left:221px;top:10px}
  .flyer--stellplatz .price-box{left:220px;top:19px}
  .price{font-size:25px;font-weight:500;line-height:1}
  .price small{font-size:12px;font-weight:500;margin-left:4px}
  .price-list{list-style:none;margin-top:8px;padding-left:0}
  .price-list li{display:flex;align-items:center;gap:3px;font-size:10.6px;font-weight:500;line-height:15.8px;margin-left:-6px;white-space:nowrap}
  .price-list svg{width:9px;height:9px;flex:none}
  .price-list sup{font-size:7px;line-height:0;vertical-align:5px;margin-right:2px}

  .info-box{position:absolute;left:16px;width:393px;border:2px solid var(--line);border-radius:5px;background:linear-gradient(180deg,#fff 0%,var(--panel) 100%)}
  .flyer--container .info-box{top:594px;height:182px;padding:11px 14px 0 15px}
  .flyer--stellplatz .info-box{top:414px;height:352px}
  .intro{font-size:11.7px;line-height:20.8px}
  .features{display:grid;grid-template-columns:196px 1fr;row-gap:4px;margin-top:9px}
  .features div{display:flex;align-items:center;gap:8px;font-weight:500;font-size:15px;color:var(--navy)}
  .features svg{width:14px;height:14px;flex:none}

  .benefit-heading{position:absolute;left:14px;font-size:17.5px;font-weight:500;color:var(--navy)}
  .benefit-text{position:absolute;left:118px;width:256px;font-size:11.7px;line-height:20.8px}
  .benefit-icon{position:absolute;left:40px}

  .footnote{position:absolute;left:32px;top:777px;font-size:6.6px;color:#444}

  .footer{position:absolute;left:0;bottom:0;width:100%;height:61px;background:var(--navy);color:#fff;font-weight:500;font-size:12.4px;letter-spacing:.3px;display:flex;flex-direction:column;align-items:center;justify-content:center;gap:5px}
  .footer p{display:flex;align-items:center;gap:5px}
  .footer .contact{gap:12px}
  .footer .contact span{display:flex;align-items:center;gap:4px}
  .footer svg{width:10px;height:10px;flex:none}
</style>
</head>
<body>
<svg width="0" height="0" style="position:absolute" aria-hidden="true">
  <symbol id="tick-circle" viewBox="0 0 20 20"><circle cx="10" cy="10" r="10" fill="#fff"/><path d="M5.5 10.3l3 3 6-6.3" fill="none" stroke="#a51c2a" stroke-width="2.6" stroke-linecap="round" stroke-linejoin="round"/></symbol>
  <symbol id="tick-navy" viewBox="0 0 20 20"><circle cx="10" cy="10" r="10" fill="#fff"/><path d="M5.5 10.3l3 3 6-6.3" fill="none" stroke="#132a4d" stroke-width="2.8" stroke-linecap="round" stroke-linejoin="round"/></symbol>
  <symbol id="pin" viewBox="0 0 20 20"><path d="M10 1a6 6 0 0 0-6 6c0 5 6 12 6 12s6-7 6-12a6 6 0 0 0-6-6zm0 8.5a2.5 2.5 0 1 1 0-5 2.5 2.5 0 0 1 0 5z" fill="#fff"/></symbol>
  <symbol id="person" viewBox="0 0 20 20"><circle cx="10" cy="6" r="4.5" fill="#fff"/><path d="M2 19c0-5 3.5-7.5 8-7.5s8 2.5 8 7.5z" fill="#fff"/></symbol>
  <symbol id="mail" viewBox="0 0 20 20"><rect x="1" y="4" width="18" height="12" fill="#fff"/><path d="M1 4l9 7 9-7" fill="none" stroke="#132a4d" stroke-width="1.6"/></symbol>
  <symbol id="globe" viewBox="0 0 20 20"><g fill="none" stroke="#fff" stroke-width="1.6"><circle cx="10" cy="10" r="8"/><ellipse cx="10" cy="10" rx="3.5" ry="8"/><path d="M2 10h16M4 5.5h12M4 14.5h12"/></g></symbol>
</svg>

<!-- Seite A -->
<section class="flyer flyer--container">
  <header class="header"><span class="brand-dot"></span><span class="brand-name">3x-Kammerhof</span></header>
  <div class="claim-band">
    <span><svg><use href="#tick-circle"/></svg>Günstig</span>
    <span><svg><use href="#tick-circle"/></svg>Sicher</span>
    <span><svg><use href="#tick-circle"/></svg>Lagern</span>
  </div>
  <div class="photo" role="img" aria-label="Foto: Reihe blauer Lagercontainer auf dem Gelände vor Bäumen und blauem Himmel"></div>
  <div class="badge"><div class="badge-inner"><div class="badge-core">
    <span class="big">1 MONAT</span>
    <span class="bigger">KOSTENFREI!</span>
    <span class="small">bei einer Anmietung<br>ab 3 Monaten</span>
  </div></div></div>

  <h2 class="section-title">VERMIETUNG VON LAGERCONTAINERN</h2>
  <div class="offer-area">
    <div class="product-image" role="img" aria-label="Abbildung: geöffneter blauer Lagercontainer mit gestapelten Holzkisten"></div>
    <div class="price-box">
      <p class="price">148,- €<small>pro Monat*</small></p>
      <ul class="price-list">
        <li><svg><use href="#tick-navy"/></svg><span>Durchgehend zugänglich</span></li>
        <li><svg><use href="#tick-navy"/></svg><span>14m<sup>2</sup>Lagerkapazität</span></li>
        <li><svg><use href="#tick-navy"/></svg><span>Versicherungsschutz möglich</span></li>
        <li><svg><use href="#tick-navy"/></svg><span>Zutrittskontrolle</span></li>
        <li><svg><use href="#tick-navy"/></svg><span>Videoüberwachung</span></li>
      </ul>
    </div>
  </div>

  <div class="info-box">
    <p class="intro">3x-Kammerhof vermietet Container zu kleinem Preis und Top-Konditonen für die Lagerung privater oder gewerblicher Güter – auch als kurzfristige Lösung (z.B. bei Umzug) geeignet. Dabei steht bei uns die Sicherheit an erster Stelle.</p>
    <div class="features">
      <div><svg viewBox="0 0 20 20"><rect x="1" y="5" width="12" height="10" rx="1.5" fill="#132a4d"/><path d="M13 9l6-3.5v9L13 11z" fill="#132a4d"/></svg>Videoüberwachung</div>
      <div><svg viewBox="0 0 20 20"><rect x="3" y="9" width="14" height="10" rx="1.5" fill="#132a4d"/><path d="M6 9V6a4 4 0 0 1 8 0v3" fill="none" stroke="#132a4d" stroke-width="2.2"/></svg>Sicherheitsschloss</div>
      <div><svg viewBox="0 0 20 20"><circle cx="10" cy="10" r="8" fill="none" stroke="#132a4d" stroke-width="2.2"/><circle cx="10" cy="10" r="3.5" fill="#132a4d"/></svg>Zutrittskontrolle</div>
      <div><svg viewBox="0 0 20 20"><path d="M2 7h4l5-4v14l-5-4H2z" fill="#132a4d"/><path d="M13.5 7a4 4 0 0 1 0 6M15.5 4.5a7.5 7.5 0 0 1 0 11" fill="none" stroke="#132a4d" stroke-width="1.8"/></svg>Alarmanlage</div>
      <div><svg viewBox="0 0 20 20"><rect x="6" y="7" width="7" height="12" rx="2" fill="#132a4d"/><rect x="8" y="3" width="3" height="4" fill="#132a4d"/><path d="M11 4h5l1 2" fill="none" stroke="#132a4d" stroke-width="1.6"/></svg>Brandmeldeanlage</div>
      <div><svg viewBox="0 0 20 20"><path d="M10 1.5a6 6 0 0 0-3.5 10.9V14h7v-1.6A6 6 0 0 0 10 1.5z" fill="none" stroke="#132a4d" stroke-width="2"/><rect x="7" y="15.5" width="6" height="2.8" rx="1" fill="#132a4d"/></svg>Licht</div>
    </div>
  </div>

  <footer class="footer">
    <p><svg><use href="#pin"/></svg>Lindenhofstraße 27 im Gewerbegebiet Nordfeld</p>
    <p class="contact"><span><svg><use href="#person"/></svg>01234 5550199</span><span><svg><use href="#mail"/></svg>ft@3x-kammerhof.de</span><span><svg><use href="#globe"/></svg>3x-kammerhof.de</span></p>
  </footer>
</section>

<!-- Seite B -->
<section class="flyer flyer--stellplatz">
  <header class="header"><span class="brand-dot"></span><span class="brand-name">3x-Kammerhof</span></header>
  <div class="claim-band">
    <span><svg><use href="#tick-circle"/></svg>Günstig</span>
    <span><svg><use href="#tick-circle"/></svg>Sicher</span>
    <span><svg><use href="#tick-circle"/></svg>Lagern</span>
  </div>

  <h2 class="section-title">STELLFLÄCHEN FÜR WOHNMOBILE / BOOTE</h2>
  <div class="offer-area">
    <div class="product-image" role="img" aria-label="Abbildung: weißes Wohnmobil in Seitenansicht"></div>
    <div class="price-box">
      <p class="price">148,- €<small>pro Monat*</small></p>
      <ul class="price-list">
        <li><svg><use href="#tick-navy"/></svg><span>Durchgehend zugänglich</span></li>
        <li><svg><use href="#tick-navy"/></svg><span>14m<sup>2</sup>Lagerkapazität</span></li>
        <li><svg><use href="#tick-navy"/></svg><span>Versicherungsschutz möglich</span></li>
        <li><svg><use href="#tick-navy"/></svg><span>Zutrittskontrolle</span></li>
        <li><svg><use href="#tick-navy"/></svg><span>Videoüberwachung</span></li>
      </ul>
    </div>
  </div>

  <div class="info-box">
    <h3 class="benefit-heading" style="top:17px">Mehr Platz</h3>
    <svg class="benefit-icon" style="top:71px" width="50" height="50" viewBox="0 0 50 50" aria-hidden="true"><rect x="14" y="1" width="21" height="21" rx="3" fill="#132a4d"/><rect x="1" y="27" width="21" height="21" rx="3" fill="#132a4d"/><rect x="28" y="27" width="21" height="21" rx="3" fill="#132a4d"/></svg>
    <p class="benefit-text" style="top:22px">Verschaffen Sie sich mehr Platz! Ob privat (Umzug, fehlende Garage, voller Keller) oder gewerblich (zur Lagerung von Akten, Geräte-park, Warenlager) – nutzen Sie Lagercontainer zur Platzoptimierung.</p>

    <h3 class="benefit-heading" style="top:135px">Ebenerdig</h3>
    <svg class="benefit-icon" style="top:189px" width="52" height="34" viewBox="0 0 52 34" aria-hidden="true"><rect x="15" y="1" width="21" height="21" rx="3" fill="#132a4d"/><rect x="0" y="29" width="52" height="4" fill="#132a4d"/></svg>
    <p class="benefit-text" style="top:146px">Auf dem befestigten Gelände können Sie auch mit großen Fahrzeugen direkt an die Lager-container heranfahren und bequem be- oder entladen, ohne große Wege gehen zu müssen.</p>

    <h3 class="benefit-heading" style="top:239px">Rentabel</h3>
    <svg class="benefit-icon" style="top:284px" width="42" height="42" viewBox="0 0 42 42" aria-hidden="true"><circle cx="21" cy="21" r="19.5" fill="none" stroke="#132a4d" stroke-width="3"/><circle cx="21" cy="21" r="15.5" fill="#132a4d"/><text x="21" y="28" text-anchor="middle" font-family="Ubuntu, sans-serif" font-weight="700" font-size="20" fill="#fff">€</text></svg>
    <p class="benefit-text" style="top:250px">Nutzen Sie den Platz in Ihrer Wohnung oder Firma rentabler und lagern Sie die wichtigen, aber nicht täglich benötigten Dinge in einen günstigen Lagerraum aus.</p>
  </div>

  <p class="footnote">*Preis gilt pro Monat und Container für private Vermietung, bei gewerblicher Anmietung zzgl. 19% MwSt</p>

  <footer class="footer">
    <p><svg><use href="#pin"/></svg>Lindenhofstraße 27 im Gewerbegebiet Nordfeld</p>
    <p class="contact"><span><svg><use href="#person"/></svg>01234 5550199</span><span><svg><use href="#mail"/></svg>ft@3x-kammerhof.de</span><span><svg><use href="#globe"/></svg>3x-kammerhof.de</span></p>
  </footer>
</section>
</body>
</html>
```